Startup online payment business - Sporting / Golf, Swift Tee payment

Background:
Our business name is "Swift Tee" we provide online payments for golfing services via our website. We currently have a logo used on our website. No other design style has been developed. Our aim is to remove cash payments for service at golf clubs.

Our Key Values:
Quick and easy
Formal and polite
Fun with professional boundary
Mate-ship relationships
100% online digital

What we want from you:
Marketing design to be used on posters and stickers in a retail setting to direct customers to our online payment Chanel.
Design must incorporate attached logo, URL swifttee.com.au and our key values can act as a guide the type of design. We have used color Hex#007672 for logo background. We are open to use other colors.

Target Market(s)

Golf clubs and golf players

Industry/Entity Type

Golf Course

Font styles to use
Sans Serif

Requirements
Must have
• Directions to online payment via URL: swifttee.com.au
Nice to have
• We like the idea of the slogan: No Cash - No worries. Have attached home screen that will be available from URL link. Consideration if using mobile phone in image. Push the online payment and steps 1. Visit swifttee.com 2. Select club 3. Confirm payment
Should not have
• Cartoons

```html
<!DOCTYPE html>
<html lang="en">
<head>
<meta charset="utf-8">
<title>Swift Tee – No Cash No Worries Poster</title>
<link rel="stylesheet" href="https://fonts.googleapis.com/css2?family=Montserrat:wght@500;600;700&family=Roboto:wght@400;500&family=Roboto+Condensed:wght@400&family=Archivo+Black&display=swap">
<style>
  :root {
    --teal: #007672;
    --teal-overlay: rgba(0,118,114,.9);
    --charcoal: #444444;
    --ring: #3b3b3b;
    --ink: #111111;
    --paper: #ffffff;
    --backdrop: #2a2a2a;
  }
  * { margin: 0; padding: 0; box-sizing: border-box; }
  html, body { width: 1200px; height: 1200px; overflow: hidden; background: var(--backdrop); }
  .poster {
    position: absolute; left: 172px; top: 0;
    width: 865px; height: 1212px;
    background: var(--paper);
    transform: scale(0.99); transform-origin: top left;
    overflow: hidden;
    font-family: "Roboto", sans-serif;
  }
  .hero-photo {
    position: absolute; left: 0; top: 0; width: 865px; height: 596px;
    background:
      radial-gradient(ellipse at 30% 25%, #c79a7d 0%, rgba(150,110,85,.6) 22%, transparent 45%),
      radial-gradient(ellipse at 75% 45%, #e8eef3 0%, rgba(200,210,225,.7) 14%, transparent 30%),
      radial-gradient(ellipse at 45% 60%, #b8c6de 0%, #8f9fbf 35%, transparent 60%),
      linear-gradient(120deg, #3e3a36 0%, #5a4d44 40%, #4a4a50 70%, #2f2f33 100%);
  }
  .brand-panel {
    position: absolute; left: 15px; top: 364px; width: 431px; height: 496px;
    background: var(--teal);
  }
  .brand-name {
    position: absolute; left: 15px; top: 440px; width: 431px; text-align: center;
    font-family: "Montserrat", sans-serif; font-weight: 600; font-size: 60px;
    color: var(--paper); letter-spacing: 1px;
  }
  .slogan {
    position: absolute; left: 38px; top: 618px;
    font-family: "Montserrat", sans-serif; font-weight: 700; font-size: 56px;
    line-height: 70px; color: var(--paper); white-space: nowrap;
  }
  .digital-badge {
    position: absolute; left: 70px; top: 770px; width: 320px; height: 320px;
    border-radius: 50%; background: var(--paper); border: 24px solid var(--ring);
    display: flex; flex-direction: column; align-items: center; justify-content: center;
    font-family: "Archivo Black", sans-serif; line-height: 58px;
  }
  .digital-badge .percent { color: var(--teal); font-size: 58px; }
  .digital-badge .word { color: var(--ink); font-size: 58px; }
  .steps-title {
    position: absolute; left: 477px; top: 608px; width: 309px; height: 46px;
    background: var(--charcoal); color: var(--paper);
    font-family: "Montserrat", sans-serif; font-weight: 700; font-size: 30px;
    line-height: 46px; text-align: center;
  }
  .steps { position: absolute; left: 484px; top: 670px; list-style: none; }
  .step-line {
    position: absolute; left: 503px; top: 700px; height: 130px;
    border-left: 2px dotted var(--ink);
  }
  .step {
    position: absolute; left: 0; display: flex; align-items: center;
    font-size: 25px; font-weight: 500; color: var(--ink); white-space: nowrap;
  }
  .step-num {
    width: 40px; height: 40px; border-radius: 50%; background: var(--teal);
    color: var(--paper); font-size: 22px; display: flex; align-items: center;
    justify-content: center; margin-right: 18px;
  }
  .pitch { position: absolute; left: 492px; top: 880px; width: 350px; color: var(--ink); }
  .pitch h2 {
    font-family: "Montserrat", sans-serif; font-weight: 700; font-size: 26px;
    line-height: 30px; margin-bottom: 16px;
  }
  .pitch p {
    font-family: "Roboto Condensed", sans-serif; font-size: 16px; line-height: 20px;
    margin-bottom: 5px;
  }
  .footer {
    position: absolute; left: 0; top: 1106px; width: 865px; height: 106px;
    background: var(--charcoal); color: var(--paper); text-align: center;
    font-family: "Montserrat", sans-serif;
  }
  .footer .invite { font-size: 23px; font-weight: 500; margin-top: 14px; }
  .footer .url {
    font-size: 26px; font-weight: 700; letter-spacing: 2px; margin-top: 6px;
    display: inline-flex; align-items: center; gap: 10px;
  }
</style>
</head>
<body>
<div class="poster">
  <div class="hero-photo" role="img" aria-label="Photo of a smiling woman holding up a smartphone showing the Swift Tee payment screen"></div>

  <div class="brand-panel"></div>
  <div class="brand-name">Swift Tee</div>

  <div class="slogan">NO CASH<br>NO WORRIES</div>

  <div class="digital-badge">
    <span class="percent">100%</span>
    <span class="word">Online</span>
    <span class="word">Digital</span>
  </div>

  <div class="steps-title">Steps to follow :</div>
  <div class="step-line"></div>
  <ol class="steps">
    <li class="step" style="top:0"><span class="step-num">1</span>Visit swifttee.com.au</li>
    <li class="step" style="top:67px"><span class="step-num">2</span>&nbsp;Select Club</li>
    <li class="step" style="top:140px"><span class="step-num">3</span>Confirm Payment</li>
  </ol>

  <div class="pitch">
    <h2>We are keen to push<br>mobile online payments</h2>
    <p>Swift Tee is here to support Golf Clubs embrace new strategies for success in a rapidly changing world</p>
    <p>Interested in learning more about how we can help grow your Clubs earning potential?</p>
    <p>Register your interest now and a member of the Swift Tee team will be in contact to advise of the services</p>
  </div>

  <footer class="footer">
    <div class="invite">Please visit our webiste for more information &amp; knowledge</div>
    <div class="url">
      <svg width="22" height="22" viewBox="0 0 24 24" fill="none" stroke="#fff" stroke-width="1.6" aria-hidden="true">
        <circle cx="12" cy="12" r="10"/><ellipse cx="12" cy="12" rx="4.5" ry="10"/>
        <line x1="2" y1="12" x2="22" y2="12"/><line x1="4" y1="7" x2="20" y2="7"/><line x1="4" y1="17" x2="20" y2="17"/>
      </svg>
      swifttee.com.au
    </div>
  </footer>
</div>
</body>
</html>
```